Packaging design for high end, natural skin care line needed

Marisa Holloway Beauty needs a label design. It is a new skin care line I am launching.
For years my line Pure Meadow Beauty was quite popular and featured in several magazines, but for personal reasons had to be shut down. Now I am launching a new line featuring PMB's top selling products, but focused solely on skin care more so than cosmetics. All products will still be handmade, but the line should still look professional-something worthy of a Fresh Larder shelf!
I am branding it with my name, as I am often quoted in articles related to gluten in beauty products, so Marisa Holloway and beauty are key words.
The key products will be facial and body serums which are packaged in .5oz., 1oz. and larger amber glass bottles with black dropper tops, I will include pictures below. For dimensions, the labels can be any size that you think will work best, but need to at the least fit the 1oz. bottle, dimensions shown here http://www.brightvialshop.example/amber-glass-round-vial/p/QX7T-52/
I loved the former PMB logo, but for Marisa Holloway Beauty I am looking for something more personal, more apothecary-like, and probably less colorful.
The line will be small, just a handful of products, but luxe, rich.
I am attaching photos of Pure Meadow Beauty's packaging for your reference.
Thanks much!!
Updates

Hi Everyone! Thank you for your submissions! Please see the links I provided in the brief, I really am looking for something more technical looking, like an apothecary. And want black text on a white background, not a black background, and nothing flowery.
Thank you all!!
Marisa

Target Market(s)

My clients are primarily women of all ages, but with more of a skin care focus, and no longer a cosmetic one, I would also like to appeal to a male audience. My clients are health conscious, gluten-free, natural, paleo, or vegan, etc. Target age is probably 25-55. Products are a bit high end, priced $45-65.

Industry/Entity Type

Cosmetics

Requirements
Must have
• It must at least say Marisa Holloway, or can say Marisa Holloway Beauty, but "Beauty" is not necessary. And capitalization is open, try whatever you think serves the brand. Likely slogans or taglines that can be included but are not essential: Care for your skin. Love and care for your skin. Handmade with love in the USA. Handmade in the USA. Think modern day apothecary. Small batch scotch. Something fine, but custom, handmade.
Nice to have
• I like the aesthetic of Tolmi Skin Care a bit http://www.rosalindtarvey.example.au/
And of Dorian Pelku as shown here http://www.pinboardly.example/pin/584203917660218447/
Also of something like this that is even customizable http://www.pinboardly.example/pin/76920418835102734/
Every product is handmade in small batches, with fine ingredients, a moderate price point of around $45-$65. And I will likely begin making custom orders. So there could be a space to say when it was made, or for whom. I would like to keep the colors classic though, I probably want to stay away from the bright pink on this one.
Should not have
• As I mentioned, probably want to stay away from a lot of color. I like black vs. gray for the text, as it will show up better in editorials. I must look good, but also photograph well. Thanks!

```html
<!DOCTYPE html>
<html lang="en">
<head>
<meta charset="utf-8">
<title>Marisa Holloway — Body Serum Label</title>
<link href="https://fonts.googleapis.com/css2?family=EB+Garamond:wght@400;500&display=swap" rel="stylesheet">
<style>
  :root {
    --page-bg: #ffffff;
    --label-pink: #f9e4e0;
    --ink: #2b1f1c;
  }
  html, body {
    margin: 0;
    padding: 0;
    width: 900px;
    height: 1200px;
    overflow: hidden;
    background: var(--page-bg);
  }
  .canvas {
    position: relative;
    width: 900px;
    height: 1200px;
    background: var(--page-bg);
  }
  .label {
    position: absolute;
    left: 150px;
    top: 230px;
    width: 600px;
    height: 740px;
    background: var(--label-pink);
    color: var(--ink);
    font-family: "EB Garamond", Garamond, serif;
    text-align: center;
  }
  .label > * {
    position: absolute;
    left: 0;
    width: 100%;
    margin: 0;
  }
  .brand-dot {
    top: 120px;
    left: 50%;
    width: 30px;
    height: 30px;
    margin-left: -15px;
    border-radius: 50%;
    background: var(--ink);
  }
  .brand-name {
    top: 168px;
    font-size: 62px;
    font-weight: 400;
    line-height: 74px;
    letter-spacing: 1px;
    text-transform: uppercase;
  }
  .tagline {
    top: 328px;
    font-size: 22px;
    line-height: 30px;
  }
  .product-name {
    top: 430px;
    font-size: 60px;
    font-weight: 400;
    line-height: 72px;
  }
  .volume {
    top: 662px;
    font-size: 28px;
    line-height: 36px;
  }
</style>
</head>
<body>
  <main class="canvas">
    <section class="label" aria-label="Body serum label">
      <span class="brand-dot" aria-hidden="true"></span>
      <h1 class="brand-name">Marisa<br>Holloway</h1>
      <p class="tagline">Handmade with love in the USA</p>
      <h2 class="product-name">Body Serum</h2>
      <p class="volume">1oz.</p>
    </section>
  </main>
</body>
</html>
```